Test and Tag business card design

We are an appliance test and tag company in Brisbane Australia requiring a business card design.
I don't have a logo.
Card front: Matte black background with white font.
Card back: White background with black font colour
Examples are attached
Minimalist design
Reason: Looking for more designs with an extreme minimal feel
Industry/Entity Type
Appliance
Contact Information for Business Card
Business name: Summit Check and Label
Description: Onsite Electrical Testing and Tagging
Licence No. 48213
Name: Greg Palmby
Mobile: 0417 592 348
Email: greg@summitcheckandlabel.com.au
Web: summitcheckandlabel.com.au
Logo Text
Summit Check and Label
Look and feel

```html
<!DOCTYPE html>
<html lang="en">
<head>
<meta charset="utf-8">
<title>Summit Check &amp; Label – Business Cards</title>
<link href="https://fonts.googleapis.com/css2?family=Open+Sans:wght@400&family=Tinos&display=swap" rel="stylesheet">
<style>
  :root {
    --stage-inner: #3a3a3a;
    --stage-outer: #141414;
    --card-white: #ffffff;
    --card-black: #151515;
    --card-black-soft: #2a2a2a;
    --ink-dark: #111111;
    --ink-light: #f2f2f2;
    --rule-light: #e6e6e6;
  }
  * { margin: 0; padding: 0; box-sizing: border-box; }
  html, body { width: 1200px; height: 1200px; overflow: hidden; }
  body {
    background: radial-gradient(ellipse at 50% 40%, var(--stage-inner) 0%, var(--stage-outer) 80%);
    position: relative;
    font-family: "Open Sans", Arial, sans-serif;
  }
  .card {
    position: absolute;
    left: 220px;
    width: 760px;
    height: 465px;
    box-shadow: 0 12px 30px rgba(0,0,0,0.55);
  }
  /* Back side: white */
  .card--back {
    top: 70px;
    background: var(--card-white);
    color: var(--ink-dark);
  }
  .brand {
    display: flex;
    align-items: center;
    gap: 12px;
    font-family: "Open Sans", Arial, sans-serif;
    font-weight: 400;
    white-space: nowrap;
  }
  .brand__mark {
    display: block;
    width: 40px;
    height: 40px;
    background: currentColor;
  }
  .card--back .brand {
    position: absolute;
    left: 0; right: 0;
    top: 170px;
    justify-content: center;
    font-size: 50px;
    letter-spacing: -0.5px;
  }
  .card--back .web {
    position: absolute;
    right: 60px;
    bottom: 52px;
    font-family: "Tinos", "Times New Roman", serif;
    font-size: 34px;
  }
  /* Front side: black */
  .card--front {
    top: 665px;
    color: var(--ink-light);
    overflow: hidden;
  }
  .card__texture {
    position: absolute;
    inset: 0;
    background: radial-gradient(ellipse at 45% 35%, var(--card-black-soft) 0%, var(--card-black) 75%);
  }
  .front-logo {
    position: absolute;
    left: 48px;
    top: 38px;
  }
  .front-logo .brand {
    font-size: 48px;
    line-height: 1.1;
  }
  .front-logo .brand__mark { width: 46px; height: 46px; }
  .front-logo .brand__line2 {
    font-size: 62px;
    line-height: 1.15;
    padding-left: 58px;
    border-top: 2px solid var(--rule-light);
    margin-top: 8px;
    padding-top: 2px;
    width: 520px;
  }
  .tagline {
    position: absolute;
    left: 48px;
    top: 212px;
    width: 520px;
    border-top: 2px solid var(--rule-light);
    padding-top: 8px;
    font-size: 25px;
  }
  .person {
    position: absolute;
    left: 110px;
    top: 300px;
    font-family: "Tinos", "Times New Roman", serif;
  }
  .person__name { font-size: 40px; }
  .person__licence { font-size: 21px; margin-top: 4px; padding-left: 30px; }
  .contact {
    position: absolute;
    right: 48px;
    top: 310px;
    font-family: "Tinos", "Times New Roman", serif;
    font-size: 22px;
    line-height: 1.35;
    list-style: none;
  }
</style>
</head>
<body>
  <section class="card card--back" aria-label="Card back">
    <div class="brand"><span class="brand__mark"></span><span>Summit Check &amp; Label</span></div>
    <p class="web">summitcheckandlabel.com.au</p>
  </section>

  <section class="card card--front" aria-label="Card front">
    <div class="card__texture" role="img" aria-label="Subtle dark woven plaid texture"></div>
    <div class="front-logo">
      <div class="brand"><span class="brand__mark"></span><span>Summit</span></div>
      <div class="brand brand__line2">Check &amp; Label</div>
    </div>
    <p class="tagline">Onsite Electrical Testing and Tagging</p>
    <div class="person">
      <p class="person__name">Greg Palmby</p>
      <p class="person__licence">Licence No. 48213</p>
    </div>
    <ul class="contact">
      <li>Mobile: 0417 592 348</li>
      <li>Email: greg@summitcheckandlabel.com.au</li>
      <li>Web: summitcheckandlabel.com.au</li>
    </ul>
  </section>
</body>
</html>
```